Healthy lifestyle Influencer business card

I need your creativity to have a business card that I can leave in all the restaurants, hotels and spas I visit to inform them that I am an influencer specializing in the wellness sector and that I will write a review about them. You can use my instagram photos Lunavivo27 or on my website www.piattileggerisani.it. I would like my business card to impress with its creativity! thank you very much!

Contact Information for Business Card

siteweb, instagram, phone number

Font styles to use
Decorative
Script

Colors
0094D4
00A9DD
6FCCEA
C7EBF8
E9F6FB
59FF00
82FF00
B8FF75
E3FFCB
F4FFEA
FFC000
F8CF3A
FAE287
FDF2CF
FEFAEE
F0912C
F2A743
F7CA91
FBE8D2
FDF5EE
EE7325
F08F49
F5BC92
FAE3D3
FDF4ED
EB3D1F
EC4F4E
F09395
F8D3D4
FCEDEE
E54698
E96AAD
F1A4CE
F9D9EA
FCEFF6

Requirements
Nice to have
• creativity

```html
<!DOCTYPE html>
<html lang="it">
<head>
<meta charset="utf-8">
<title>Luna Vivo Chef – Biglietto da visita</title>
<link rel="stylesheet" href="https://fonts.googleapis.com/css2?family=Mulish:wght@400;500;600&display=swap">
<style>
  :root {
    --bg: #b9b9b9;
    --card-white: #ffffff;
    --sage: #95b4ac;
    --slate: #6d6b6d;
    --ink: #1f1f1f;
    --brand-grey: #6a6a6a;
    --on-sage: #ffffff;
  }
  * { box-sizing: border-box; margin: 0; padding: 0; }
  html, body { width: 1200px; height: 1200px; overflow: hidden; }
  body {
    background: var(--bg);
    font-family: "Mulish", sans-serif;
    position: relative;
  }
  .card {
    position: absolute;
    left: 228px;
    width: 746px;
    height: 430px;
    overflow: hidden;
  }
  .card-front { top: 113px; background: var(--card-white); }
  .card-back { top: 583px; background: var(--sage); }

  .brand-block {
    position: absolute;
    left: 40px;
    top: 206px;
    width: 320px;
    text-align: center;
    color: var(--brand-grey);
  }
  .brand-name {
    font-size: 35px;
    font-weight: 500;
    letter-spacing: 0.5px;
    line-height: 1;
  }
  .brand-tagline {
    margin-top: 12px;
    font-size: 15px;
    font-weight: 600;
  }

  .divider {
    position: absolute;
    left: 386px;
    top: 135px;
    width: 2px;
    height: 190px;
    background: var(--sage);
  }
  .address {
    position: absolute;
    left: 413px;
    top: 136px;
    font-size: 19px;
    font-weight: 500;
    line-height: 27px;
    color: var(--ink);
  }
  .contact-list {
    position: absolute;
    left: 421px;
    top: 202px;
    list-style: none;
  }
  .contact-item {
    display: flex;
    align-items: center;
    height: 33px;
    font-size: 19px;
    font-weight: 500;
    color: var(--ink);
  }
  .contact-icon {
    width: 18px;
    height: 18px;
    margin-right: 10px;
    flex: none;
  }
  .footer-band {
    position: absolute;
    left: 0;
    bottom: 0;
    width: 746px;
    height: 28px;
  }

  .back-brand {
    position: absolute;
    left: 0;
    right: 0;
    top: 172px;
    text-align: center;
    color: var(--on-sage);
  }
  .back-name {
    font-size: 72px;
    font-weight: 500;
    letter-spacing: 1px;
    line-height: 1;
  }
  .back-tagline {
    margin-top: 22px;
    font-size: 30px;
    font-weight: 600;
  }
</style>
</head>
<body>

<section class="card card-front">
  <div class="brand-block">
    <p class="brand-name">Luna Vivo Chef</p>
    <p class="brand-tagline">Leggera con i piatti del cuore</p>
  </div>

  <div class="divider"></div>

  <p class="address">Via delle Erbe 12<br>Scala B Interno 4</p>

  <ul class="contact-list">
    <li class="contact-item">
      <svg class="contact-icon" viewBox="0 0 20 20" aria-hidden="true">
        <path d="M5 2 L8 2 L9 6 L7 8 Q9 12 12 13 L14 11 L18 12 L18 15 Q18 18 15 18 Q3 17 2 5 Q2 2 5 2 Z" fill="none" stroke="var(--sage)" stroke-width="1.6"/>
      </svg>
      555-010-4821
    </li>
    <li class="contact-item">
      <svg class="contact-icon" viewBox="0 0 20 20" aria-hidden="true">
        <rect x="1" y="4" width="18" height="12" fill="var(--sage)"/>
        <path d="M1 4 L10 11 L19 4" fill="none" stroke="#fff" stroke-width="1.4"/>
      </svg>
      info@piattileggerisani
    </li>
    <li class="contact-item">
      <svg class="contact-icon" viewBox="0 0 20 20" aria-hidden="true">
        <circle cx="10" cy="10" r="8.5" fill="var(--sage)"/>
        <path d="M1.5 10 H18.5 M10 1.5 Q5 10 10 18.5 M10 1.5 Q15 10 10 18.5" fill="none" stroke="#fff" stroke-width="1"/>
      </svg>
      www.piattileggerisani
    </li>
    <li class="contact-item">
      <svg class="contact-icon" viewBox="0 0 20 20" aria-hidden="true">
        <circle cx="10" cy="10" r="8" fill="none" stroke="var(--sage)" stroke-width="1.6"/>
      </svg>
      @piattileggerisani
    </li>
  </ul>

  <svg class="footer-band" viewBox="0 0 746 28" aria-hidden="true">
    <polygon points="0,0 391,0 363,28 0,28" fill="var(--slate)"/>
    <polygon points="421,0 746,0 746,28 393,28" fill="var(--sage)"/>
  </svg>
</section>

<section class="card card-back">
  <div class="back-brand">
    <p class="back-name">Luna Vivo Chef</p>
    <p class="back-tagline">Leggera con i piatti del cuore</p>
  </div>
</section>

</body>
</html>
```